The Copper Hour ebook cover for Desmond Okafor Whitley

I need an ebook cover/jpeg that depicts a Middle-Eastern desert and sky. The cover must be very elegant and very austere, the simpler the better.
Toward the top, the text will read: The Copper Hour
Directly below the title will read: Corvin Teague
The dimensions for the cover should be 2560 pixels (height) and 1600 pixels (width.)

Target Market(s)

Readers of serious magical realism and/or fantasy literature with a serious literary element.

Font styles to use
Serif

Requirements
Must have
• My ebook cover MUST be a painting or illustration depicting a very austere Middle-Eastern desert and desert sky. Must be elegant and austere. The lettering of the title and author name must blend in beautifully with the image--just like fine books in a bookstore. Title must appear at the top: The Copper Hour. The author's name must appear below title and read: Corvin Teague. Dimensions must be 2560 pixels (height) by 1600 pixels (width)
Nice to have
• A very austere desert on the bottom and a sad elegant sky above.
Should not have
• My ebook cover should not have a spine or a back. I just need an ebook cover of the dimensions stated above.

```html
<!DOCTYPE html>
<html lang="en">
<head>
<meta charset="utf-8">
<title>The Copper Hour — Corvin Teague</title>
<link rel="stylesheet" href="https://fonts.googleapis.com/css2?family=Italiana&family=Cinzel:wght@400&display=swap">
<style>
  :root {
    --page-bg: #ffffff;
    --cover-edge: #2a1a12;
    --sky-deep: #1f9fee;
    --sky-mid: #5cc6f2;
    --sky-haze: #9fe4f2;
    --dune-light: #e9873a;
    --dune-mid: #e0712a;
    --dune-shadow: #b9461c;
    --title-ink: #3b2216;
    --author-ink: #7fd2f6;
  }
  html, body {
    margin: 0;
    padding: 0;
    width: 1200px;
    height: 1125px;
    overflow: hidden;
    background: var(--page-bg);
  }
  .canvas {
    position: relative;
    width: 1200px;
    height: 1125px;
  }
  .cover {
    position: absolute;
    left: 296px;
    top: 70px;
    width: 630px;
    height: 1009px;
    box-sizing: border-box;
    border: 1px solid var(--cover-edge);
    overflow: hidden;
  }
  .cover-art {
    position: absolute;
    inset: 0;
    background: linear-gradient(
      to bottom,
      var(--sky-deep) 0%,
      var(--sky-mid) 25%,
      var(--sky-haze) 44%,
      var(--dune-light) 52%,
      var(--dune-mid) 75%,
      var(--dune-shadow) 100%
    );
  }
  .cover-title {
    position: absolute;
    top: 118px;
    left: 0;
    right: 0;
    margin: 0;
    text-align: center;
    font-family: "Italiana", serif;
    font-weight: 400;
    font-size: 118px;
    line-height: 0.72;
    color: var(--title-ink);
    letter-spacing: -1px;
  }
  .cover-title span { display: block; }
  .cover-author {
    position: absolute;
    top: 908px;
    left: 0;
    right: 0;
    margin: 0;
    text-align: center;
    font-family: "Cinzel", serif;
    font-weight: 400;
    font-size: 38px;
    letter-spacing: 1px;
    color: var(--author-ink);
  }
</style>
</head>
<body>
  <div class="canvas">
    <div class="cover">
      <div class="cover-art" role="img" aria-label="Photograph of a tall orange sand dune under a bright blue sky with white clouds, a small line of hikers climbing the ridge"></div>
      <h1 class="cover-title"><span>The</span><span>Copper</span><span>Hour</span></h1>
      <p class="cover-author">Corvin Teague</p>
    </div>
  </div>
</body>
</html>
```